Stationary Design For Youthful Disability Company

Hi Designers,
Looking to have our brand applied to a range of stationary items to professionalise our approach, we are a disability services company that aligns young carers with disabled youth and adults. Our stationary needs to look professional but can verge into a fun bright territory too.
Winning designer will be first contact for advertising campaign, form creation and web-design in January 2014.
Cheers,
Tom
Brightpath Disability Services
Design Briefs
Stationary.
Sleek fun and bright stationary that portrays a professional but youthful disability service. Company prides its self on delivering youthful carers to disabled clients.
Needed:
- Business Card - Letter Head - Email Signature
- Invoice / Quotation (blank branded paper) - Normal Envelope - A4 Envelope
- Stationary for future forms or documents. (Doesn't need to include all contacts, branding is enough).
Would be nice if we were able to edit numbers etc as we change them.
Include:
Thomas Wexford - Managing Director
M. 0458 927 304
E. twexford@brightpathcare.example
A. PO Box 78 Larchmere 3190
ABN. 47392051864

```html
<!DOCTYPE html>
<html lang="en">
<head>
<meta charset="utf-8">
<title>Brightpath Disability Services — Stationery</title>
<link rel="stylesheet" href="https://fonts.googleapis.com/css2?family=Arimo:wght@400;700&display=swap">
<style>
  :root {
    --backdrop: #7b4b2b;
    --paper: #f4f4f5;
    --paper-shade: #e9e9eb;
    --brand-blue: #1b9bd0;
    --rule-blue: #cfe6f1;
    --ink: #4a4a4a;
    --ink-soft: #6b6b6b;
    --watermark: #ebebed;
    --case-spine: #2a2a2c;
  }
  * { box-sizing: border-box; margin: 0; padding: 0; }
  html, body { width: 1200px; height: 1200px; overflow: hidden; }
  body {
    background: var(--backdrop);
    font-family: "Arimo", Arial, sans-serif;
    color: var(--ink);
    position: relative;
  }
  .item { position: absolute; }

  /* brand name lockup */
  .brand { display: flex; align-items: center; gap: 6px; }
  .brand-dot { width: 16px; height: 16px; border-radius: 50%; background: var(--brand-blue); flex: none; }
  .brand-name {
    font-weight: 700; color: var(--brand-blue);
    font-size: 11px; line-height: 1.1; letter-spacing: 0.2px;
  }

  .contact { font-size: 6.6px; line-height: 8.6px; color: var(--ink-soft); }
  .contact strong { font-weight: 700; color: var(--ink); }

  .watermark-disc { position: absolute; border-radius: 50%; background: var(--watermark); }

  /* A4 envelope */
  .envelope-a4 { left: 118px; top: 45px; width: 439px; height: 665px; }
  .envelope-a4 .flap { position: absolute; left: 0; top: 0; width: 100%; height: 52px; z-index: 1; }
  .envelope-a4 .body {
    position: absolute; left: 0; top: 50px; width: 100%; height: 615px;
    background: var(--paper);
  }
  .envelope-a4 .brand { position: absolute; left: 47px; top: 110px; }
  .envelope-a4 .contact { position: absolute; left: 48px; top: 538px; }
  .envelope-a4 .rule { position: absolute; left: 0; right: 0; top: 618px; height: 4px; background: var(--rule-blue); }

  /* DL envelope */
  .envelope-dl { left: 585px; top: 45px; width: 512px; height: 305px; }
  .envelope-dl .flap { position: absolute; left: 0; top: 0; width: 100%; height: 52px; z-index: 1; }
  .envelope-dl .body {
    position: absolute; left: 0; top: 50px; width: 100%; height: 255px;
    background: linear-gradient(90deg, var(--paper) 0%, var(--paper-shade) 100%);
    overflow: hidden;
  }
  .envelope-dl .brand { position: absolute; left: 45px; top: 97px; }
  .envelope-dl .contact { position: absolute; left: 45px; top: 195px; font-size: 5.8px; line-height: 7.7px; }
  .envelope-dl .rule { position: absolute; left: 0; right: 0; bottom: 0; height: 5px; background: #a9d3e8; }

  /* Letterhead */
  .letterhead {
    left: 598px; top: 378px; width: 486px; height: 628px;
    background: var(--paper); overflow: hidden;
  }
  .letterhead .brand { position: absolute; right: 52px; top: 68px; }
  .letter-text {
    position: absolute; left: 83px; top: 94px; width: 322px;
    font-size: 7.3px; line-height: 9.5px; color: var(--ink-soft);
  }
  .letter-text .recipient { font-weight: 700; color: var(--ink); margin-bottom: 34px; }
  .letter-text p { margin-bottom: 9px; }
  .letter-text .salutation { font-weight: 700; color: var(--ink); }
  .letter-text .contact { font-size: 7.1px; line-height: 9.5px; margin-top: 14px; }

  /* CD case */
  .cd-case { left: 107px; top: 838px; width: 355px; height: 319px; background: var(--paper); overflow: hidden; }
  .cd-case .spine { position: absolute; left: 0; top: 0; width: 33px; height: 100%; background: var(--case-spine); }
  .cd-case .rule { position: absolute; left: 33px; right: 0; bottom: 0; height: 5px; background: #a9d3e8; }
  .cd-case .brand-stack {
    position: absolute; left: 115px; top: 100px; width: 170px;
    display: flex; flex-direction: column; align-items: center; gap: 10px;
  }
  .cd-case .brand-stack .brand-dot { width: 56px; height: 56px; }
  .cd-case .brand-stack .brand-name { font-size: 15px; text-align: center; }
  .cd-case .contact { position: absolute; right: 18px; top: 238px; text-align: right; }

  /* Disc */
  .disc {
    left: 390px; top: 850px; width: 292px; height: 292px; border-radius: 50%;
    background: #f6f6f7; box-shadow: 0 0 0 1px #d9d9dc; overflow: hidden;
  }
  .disc .art { position: absolute; left: 60px; top: 90px; width: 240px; height: 220px; border-radius: 50%; opacity: .7;
    background: radial-gradient(circle at 30% 60%, #e8c8cc 0%, #f1dcc9 40%, #c9dfe9 75%, transparent 76%); }
  .disc .brand { position: absolute; left: 70px; top: 58px; }
  .disc .hub { position: absolute; left: 92px; top: 92px; width: 108px; height: 108px; border-radius: 50%; background: #fafafa; box-shadow: 0 0 0 1px #d0d0d3; }
  .disc .hub-ring { position: absolute; left: 118px; top: 118px; width: 56px; height: 56px; border-radius: 50%; border: 7px solid #2b2b2d; background: #ededee; }
  .disc .hole { position: absolute; left: 134px; top: 134px; width: 24px; height: 24px; border-radius: 50%; background: var(--backdrop); }
</style>
</head>
<body>

<!-- A4 envelope -->
<section class="item envelope-a4" aria-label="A4 envelope">
  <svg class="flap" viewBox="0 0 439 52" preserveAspectRatio="none" aria-hidden="true">
    <polygon points="8,0 431,0 439,52 0,52" fill="var(--brand-blue)"/>
  </svg>
  <div class="body">
    <div class="watermark-disc" style="left:120px;top:200px;width:200px;height:200px;"></div>
  </div>
  <div class="brand"><span class="brand-dot"></span><span class="brand-name">Brightpath<br>Disability Services</span></div>
  <div class="contact">
    <strong>Information :</strong><br>
    Brightpath Disability Services<br>
    Thomas Wexford - Managing Director<br>
    M. 0458 927 304<br>
    E. twexford@brightpathcare.example<br>
    A. PO Box 78 Larchmere 3190<br>
    ABN. 47392051864
  </div>
  <div class="rule"></div>
</section>

<!-- DL envelope -->
<section class="item envelope-dl" aria-label="DL envelope">
  <svg class="flap" viewBox="0 0 512 52" preserveAspectRatio="none" aria-hidden="true">
    <polygon points="14,0 498,0 512,52 0,52" fill="var(--brand-blue)"/>
  </svg>
  <div class="body">
    <div class="watermark-disc" style="left:300px;top:40px;width:180px;height:180px;"></div>
    <div class="rule"></div>
  </div>
  <div class="brand"><span class="brand-dot"></span><span class="brand-name">Brightpath<br>Disability Services</span></div>
  <div class="contact">
    <strong>Information :</strong><br>
    Brightpath Disability Services<br>
    Thomas Wexford - Managing Director<br>
    M. 0458 927 304<br>
    E. twexford@brightpathcare.example<br>
    A. PO Box 78 Larchmere 3190<br>
    ABN. 47392051864
  </div>
</section>

<!-- Letterhead -->
<section class="item letterhead" aria-label="Letterhead">
  <div class="watermark-disc" style="left:220px;top:400px;width:220px;height:220px;"></div>
  <div class="brand"><span class="brand-dot"></span><span class="brand-name">Brightpath<br>Disability Services</span></div>
  <div class="letter-text">
    <div class="recipient">Sample Company Ltd.<br>Brightpath Disability Services<br>Thomas Wexford - Managing Director</div>
    <p>September 1, 2009</p>
    <p class="salutation">To the Former Stockholders of Veritan, Inc.:</p>
    <p>We welcome you as shareholders of Harbourline Health Incorporated (Exchange : HBLH). We are pleased to inform you that on September 1, 2009, Veritan, Inc. ("Veritan") merged with a subsidiary of Harbourline Health Incorporated ("Harbourline Health"). As a result of the merger, each share of Veritan preferred stock owned by you at the time of the merger was converted into and represents the right to receive the applicable Consideration Per Share, as defined in the Agreement and Plan of Merger, plus cash in lieu of any fractional shares of Harbourline Health Common Stock, if any.</p>
    <p>Please read and follow carefully the enclosed instructions. In order to receive your Harbourline Health stock certificate and cash payment for your shares, if any, you must complete, sign, date and return the enclosed Letter of Transmittal, together with your Veritan stock certificate(s) in accordance with the provisions of the Letter of Transmittal and the enclosed instructions. Each person listed on your Veritan stock certificate(s) as a registered holder must sign the Letter of Transmittal. You should complete and sign a separate Letter of Transmittal for each certificate registered in a different name or form. Photocopies of the Letter of Transmittal may be used. If you have any questions, please contact the exchange agent, Northgate Registry &amp; Trust Company, LLC, toll free at (800) 555-0142 or at (800) 555-0178.</p>
    <p>Following receipt of your Veritan certificate(s) and properly completed Letter of Transmittal, the exchange agent will mail your Harbourline Health stock certificate and cash payment, if any, for your shares to the address shown for you in the "Account Registration" section unless you provide a different address in accordance with the special delivery instructions in the Letter of Transmittal.</p>
    <p>We are pleased to have you as a stockholder of Harbourline Health and look forward to enjoying your continued support of the combined company.</p>
    <p>Sincerely yours,</p>
    <p>HARBOURLINE HEALTH INCORPORATED</p>
    <div class="contact">
      <strong>Information :</strong><br>
      Brightpath Disability Services<br>
      Thomas Wexford - Managing Director<br>
      M. 0458 927 304<br>
      E. twexford@brightpathcare.example<br>
      A. PO Box 78 Larchmere 3190<br>
      ABN. 47392051864
    </div>
  </div>
</section>

<!-- CD case -->
<section class="item cd-case" aria-label="CD case cover">
  <div class="spine"></div>
  <div class="brand-stack">
    <span class="brand-dot"></span>
    <span class="brand-name">Brightpath<br>Disability Services</span>
  </div>
  <div class="contact">
    <strong>Information :</strong><br>
    Brightpath Disability Services<br>
    Thomas Wexford - Managing Director<br>
    M. 0458 927 304<br>
    E. twexford@brightpathcare.example<br>
    A. PO Box 78 Larchmere 3190<br>
    ABN. 47392051864
  </div>
  <div class="rule"></div>
</section>

<!-- CD disc -->
<section class="item disc" aria-label="CD disc label">
  <div class="art" role="img" aria-label="Soft pastel brand artwork across the disc face"></div>
  <div class="brand"><span class="brand-dot"></span><span class="brand-name">Brightpath<br>Disability Services</span></div>
  <div class="hub"></div>
  <div class="hub-ring"></div>
  <div class="hole"></div>
</section>

</body>
</html>
```